Email Signature Design

Please design an email signature, the below is an example of our current design;
___

CARRODY ESTATE HOLDINGS PTY LTD
BENEDICT HARLOWE
Licensed Strata and Community Manager

143 Tallowood Street,
KELDARRA NSW 2093

P: 02.9473.6820 F: 9536.2048
Website: www.carrodyestate.com.au

This e-mail message and accompanying data may contain information that is confidential and private. If you are not the intended recipient, the use, dissemination, distribution or copying of this message or data is prohibited.

If you have received this e-mail in error please notify us immediately and delete all material pertaining to this e-mail. strata@carrodyestate.com.au

___

We would like to incorporate our logo and company colours, you can view the colours and feel of image at www.carrodyestate.com.au

Industry/Entity Type

It Company

Requirements
Must have
• use of logo and company colours (image)

```html
<!DOCTYPE html>
<html lang="en">
<head>
<meta charset="utf-8">
<title>Email Signature – Carrody Estate Holdings</title>
<link href="https://fonts.googleapis.com/css2?family=Arimo:ital,wght@0,400;0,700;1,400&family=Michroma&display=swap" rel="stylesheet">
<style>
  :root {
    --ink: #333333;
    --muted: #666666;
    --gold: #94820f;
    --rule: #8a8a8a;
    --eco-green: #1d9a3a;
    --paper: #ffffff;
  }
  html, body {
    margin: 0;
    padding: 0;
    overflow: hidden;
    background: var(--paper);
  }
  .signature {
    position: relative;
    width: 1200px;
    height: 750px;
    overflow: hidden;
    background: var(--paper);
    font-family: "Arimo", Arial, sans-serif;
    color: var(--ink);
  }
  .signature > * { position: absolute; margin: 0; }

  .sign-off {
    left: 50px; top: 42px;
    font-size: 22px; font-style: italic; color: var(--ink);
  }
  .person-name {
    left: 50px; top: 222px;
    font-family: "Michroma", sans-serif;
    font-size: 25px; letter-spacing: 1px;
    color: #3a3a3a; font-weight: 400;
  }
  .person-role {
    left: 51px; top: 259px;
    font-size: 22px; color: var(--ink);
  }

  .brand-mark {
    left: 50px; top: 312px;
    width: 200px; height: 165px;
  }
  .brand-mark .brand-square {
    position: absolute; left: 70px; top: 10px;
    width: 60px; height: 60px; background: var(--gold);
  }
  .brand-mark .brand-name {
    position: absolute; left: 0; right: 0; top: 118px;
    text-align: center;
    font-size: 16px; font-weight: 700; letter-spacing: .5px;
    color: var(--gold);
  }

  .company {
    left: 262px; top: 306px;
    font-size: 24px; font-weight: 700; color: var(--muted);
  }
  .company .company-lead { color: var(--gold); }

  .contact {
    left: 260px; top: 337px;
    font-size: 22px; line-height: 29px; color: var(--ink);
  }
  .contact p { margin: 0; }
  .contact .label { font-weight: 700; }
  .contact .sep { padding: 0 10px; }
  .contact .email-line { margin-top: 5px; }
  .contact a { color: var(--muted); }
  .contact .website { color: var(--gold); text-decoration: none; }

  .social {
    left: 930px; top: 432px;
    display: flex; gap: 14px;
    list-style: none; padding: 0;
  }
  .social li {
    display: flex; align-items: center; gap: 6px;
    font-size: 14px; color: var(--muted);
    height: 52px;
  }
  .social .social-square {
    width: 14px; height: 14px; background: var(--muted);
  }

  .divider {
    left: 50px; top: 497px;
    width: 1100px; height: 0;
    border-top: 1px solid var(--rule);
  }

  .disclaimer {
    left: 50px; top: 511px; width: 1110px;
    font-size: 21px; line-height: 29px; color: var(--ink);
  }
  .disclaimer p { margin: 0 0 22px; }
  .disclaimer a { color: var(--muted); }

  .eco-icon {
    left: 50px; top: 690px;
    width: 52px; height: 48px;
  }
  .eco-note {
    left: 130px; top: 721px;
    font-size: 17px; font-style: italic; color: var(--ink);
  }
</style>
</head>
<body>
<main class="signature">
  <p class="sign-off">Yours sincerely,</p>

  <h1 class="person-name">BENEDICT HARLOWE</h1>
  <p class="person-role">Licensed Strata and Community Manager</p>

  <div class="brand-mark">
    <span class="brand-square"></span>
    <span class="brand-name">CARRODY ESTATE</span>
  </div>

  <h2 class="company"><span class="company-lead">CARRODY</span> ESTATE HOLDINGS PTY LTD</h2>

  <address class="contact" style="font-style:normal">
    <p>143 Tallowood Street,</p>
    <p>KELDARRA NSW 2093</p>
    <p><span class="label">P</span>: 02.9473.6820<span class="sep">I</span><span class="label">F</span>: 9536.2048</p>
    <p class="email-line"><span class="label">E</span>: <a href="mailto:info@carrodyestate.com.au">info@carrodyestate.com.au</a></p>
    <p>Website: <a class="website" href="http://www.carrodyestate.com.au">www.carrodyestate.com.au</a></p>
  </address>

  <ul class="social">
    <li><span class="social-square"></span>Chatterly</li>
    <li><span class="social-square"></span>Chirpline</li>
    <li><span class="social-square"></span>Linkworks</li>
  </ul>

  <div class="divider"></div>

  <section class="disclaimer">
    <p>This e-mail message and accompanying data may contain information that is confidential and private. If you are not the intended recipient, the use, dissemination, distribution or copying of this message or data is prohibited.</p>
    <p>If you have received this e-mail in error please notify us immediately and delete all material pertaining to this e-mail. <a href="mailto:strata@carrodyestate.com.au">strata@carrodyestate.com.au</a></p>
  </section>

  <svg class="eco-icon" viewBox="0 0 52 48" role="img" aria-label="Small green environment icon with trees and a winding path">
    <rect width="52" height="48" fill="var(--eco-green)"/>
  </svg>
  <p class="eco-note">Please consider the environment - do you really need to print this email?</p>
</main>
</body>
</html>
```